4 page brochure for Logistics Company

Need a 4 page brochure (ie folded A3) for a Logistics company.
Service is a virtual network of warehouse and logistics companies.
Style is professional but accessible.
We have logo and styles designed and will upload these.
We have identified example images that could be used in the brochure.
Content will be uploaded also.
Updates
Reason: A couple of designers requested more time
Am giving another 24 hours to finalise and will then select most suitable design
Target Market(s)
40 to 60 year old business owners (traditional) - Australian
Industry/Entity Type
It Company
Requirements
Must have
- Professional
Should not have
- Nothing tacky

```html
<!DOCTYPE html>
<html lang="en">
<head>
<meta charset="utf-8">
<title>Coastline Freight Network – Folder Brochure</title>
<link rel="stylesheet" href="https://fonts.googleapis.com/css2?family=Open+Sans:wght@300;400;600;700&display=swap">
<style>
  :root {
    --stage: #e4e4e4;
    --paper: #ffffff;
    --brand-blue: #1f5ea8;
    --deep-blue: #174b8e;
    --bright-blue: #2a7bc4;
    --slate: #7d8a92;
    --slate-light: #a3adb3;
    --ink: #2b2f33;
    --photo-warm: #c8bca2;
    --photo-cool: #cfd6dc;
    --on-blue: #ffffff;
  }
  * { box-sizing: border-box; margin: 0; padding: 0; }
  html, body {
    width: 1200px; height: 767px; overflow: hidden;
    background: var(--stage);
    font-family: "Open Sans", Arial, sans-serif;
  }
  .spread {
    position: absolute; left: 105px; top: 33px;
    width: 990px; height: 700px;
    display: flex;
    box-shadow: 0 14px 30px rgba(0,0,0,0.18);
  }
  .page { position: relative; width: 495px; height: 700px; overflow: hidden; background: var(--paper); }
  .page-art { position: absolute; inset: 0; }

  .brand { position: absolute; }
  .brand-name {
    display: flex; align-items: center; gap: 10px;
    font-weight: 700; font-size: 21px; line-height: 1.05;
    color: var(--brand-blue);
  }
  .brand-mark { width: 16px; height: 16px; background: var(--brand-blue); flex: none; }
  .brand-tagline {
    margin-top: 6px; padding-left: 26px;
    font-weight: 700; font-size: 12.5px; color: var(--ink); letter-spacing: 0.2px;
  }
  .back-cover .brand { left: 42px; top: 338px; }
  .front-cover .brand { right: 34px; top: 30px; text-align: left; }

  .contact-list {
    position: absolute; right: 26px; top: 570px;
    list-style: none; text-align: right;
    color: var(--on-blue); font-size: 12.5px; line-height: 22px;
  }
  .contact-list li { display: flex; justify-content: flex-end; align-items: center; gap: 8px; }
  .contact-list svg { width: 14px; height: 14px; flex: none; }

  .front-copy {
    position: absolute; left: 40px; right: 30px; top: 452px;
    text-align: center; color: var(--on-blue);
  }
  .headline { font-weight: 300; font-size: 25px; line-height: 1.2; letter-spacing: 0.3px; }
  .lede { margin-top: 16px; font-size: 12.5px; line-height: 1.45; padding: 0 18px; }
  .web-address { position: absolute; left: 0; right: 0; bottom: 28px; text-align: center; color: var(--on-blue); font-size: 12px; }
</style>
</head>
<body>
<main class="spread">

  <!-- Back cover -->
  <section class="page back-cover">
    <svg class="page-art" viewBox="0 0 495 700" width="495" height="700" aria-hidden="false">
      <defs>
        <linearGradient id="warehouseBack" x1="0" y1="0" x2="1" y2="1">
          <stop offset="0" stop-color="#6f6a5e"/>
          <stop offset="0.6" stop-color="var(--photo-warm)"/>
          <stop offset="1" stop-color="#9a9486"/>
        </linearGradient>
        <linearGradient id="blueBack" x1="0" y1="1" x2="1" y2="0">
          <stop offset="0" stop-color="var(--deep-blue)"/>
          <stop offset="0.5" stop-color="var(--bright-blue)"/>
          <stop offset="1" stop-color="var(--brand-blue)"/>
        </linearGradient>
      </defs>
      <path role="img" aria-label="Photo of forklifts inside a warehouse"
            d="M235,0 L495,0 L495,250 C410,215 300,125 235,0 Z" fill="url(#warehouseBack)"/>
      <path d="M205,0 L238,0 C300,118 405,212 495,248 L495,266 C390,236 275,140 205,0 Z" fill="var(--brand-blue)"/>
      <path d="M0,440 L495,330 L495,700 L0,700 Z" fill="var(--slate)"/>
      <path d="M0,448 L495,338" stroke="var(--paper)" stroke-width="3"/>
      <path d="M0,700 C170,640 330,520 495,400 L495,700 Z" fill="url(#blueBack)"/>
      <path d="M0,700 C170,640 330,520 495,400" fill="none" stroke="var(--paper)" stroke-width="3"/>
    </svg>

    <div class="brand">
      <div class="brand-name"><span class="brand-mark"></span>Coastline Freight Network</div>
      <div class="brand-tagline">Scale : Synergy : Value</div>
    </div>

    <ul class="contact-list">
      <li>07 5550 1820
        <svg viewBox="0 0 16 16"><path d="M4 2l2.5 3-1.5 1.5c.8 1.8 2.5 3.5 4.5 4.5L11 9.5l3 2.5-1.5 2C7 14 2 9 2 3.5z" fill="currentColor"/></svg></li>
      <li>0400 555 719
        <svg viewBox="0 0 16 16"><rect x="4" y="1" width="8" height="14" rx="1.5" fill="none" stroke="currentColor" stroke-width="1.6"/><circle cx="8" cy="12.5" r="1" fill="currentColor"/></svg></li>
      <li>sam.reeve@coastfreight.com.au
        <svg viewBox="0 0 16 16"><rect x="1.5" y="3.5" width="13" height="9" fill="none" stroke="currentColor" stroke-width="1.5"/><path d="M1.5 3.5L8 9l6.5-5.5" fill="none" stroke="currentColor" stroke-width="1.5"/></svg></li>
      <li>coastfreight.com.au
        <svg viewBox="0 0 16 16"><circle cx="8" cy="8" r="6.5" fill="none" stroke="currentColor" stroke-width="1.4"/><ellipse cx="8" cy="8" rx="3" ry="6.5" fill="none" stroke="currentColor" stroke-width="1.2"/><path d="M1.5 8h13" stroke="currentColor" stroke-width="1.2"/></svg></li>
    </ul>
  </section>

  <!-- Front cover -->
  <section class="page front-cover">
    <svg class="page-art" viewBox="0 0 495 700" width="495" height="700">
      <defs>
        <linearGradient id="warehouseFront" x1="0" y1="0" x2="1" y2="1">
          <stop offset="0" stop-color="#8d846f"/>
          <stop offset="0.5" stop-color="var(--photo-warm)"/>
          <stop offset="1" stop-color="var(--photo-cool)"/>
        </linearGradient>
        <linearGradient id="blueFront" x1="0" y1="0" x2="1" y2="1">
          <stop offset="0" stop-color="var(--brand-blue)"/>
          <stop offset="0.45" stop-color="var(--bright-blue)"/>
          <stop offset="1" stop-color="var(--deep-blue)"/>
        </linearGradient>
      </defs>
      <rect role="img" aria-label="Photo of a forklift moving between tall warehouse racks"
            x="0" y="0" width="495" height="440" fill="url(#warehouseFront)"/>
      <path d="M110,0 L495,0 L495,275 Z" fill="var(--paper)" opacity="0.78"/>
      <path d="M0,420 C180,400 340,360 495,310 L495,700 L0,700 Z" fill="var(--slate-light)"/>
      <path d="M0,450 C180,428 340,385 495,335 L495,700 L0,700 Z" fill="url(#blueFront)"/>
    </svg>

    <div class="brand">
      <div class="brand-name"><span class="brand-mark"></span>Coastline Freight<br>Network</div>
      <div class="brand-tagline">Scale : Synergy : Value</div>
    </div>

    <div class="front-copy">
      <h1 class="headline">A new solution for Australian warehouse business owners.</h1>
      <p class="lede">Offering national scale to increase revenues, achieving synergies to reduce costs, and enhancing the value in your business.</p>
    </div>
    <p class="web-address">www.coastfreight.com.au</p>
  </section>

</main>
</body>
</html>
```